The dental corner of brindlewood web page

website for dental office
Already have domain, mostly information only with address, telephone and google map and hours of operation on top. mobile friendly. SEO a most.

Target Market(s)

Local families

Industry/Entity Type

Dental Clinic

Number of Pages Required

1 page

Font styles to use
Serif

Colors

Designer to choose colors to be used in the design.

Requirements
Must have
• SEO
• Information to find the location
• mobile friendly
• dr's. biography
• services offered
• contect to social media (google, facebook, and instagram)
• Se habla espaƱol
• All insurance accepted
• request an appointment form to notify us

```html
<!DOCTYPE html>
<html lang="en">
<head>
<meta charset="utf-8">
<title>The Dental Corner of Brindlewood</title>
<link href="https://fonts.googleapis.com/css2?family=Roboto:wght@300;400;500;700&display=swap" rel="stylesheet">
<style>
:root{
  --blue:#1e6fc0;
  --blue-deep:#0d4b9c;
  --green:#3cb43c;
  --ink:#3a3a3a;
  --muted:#7a7a7a;
  --line:#d6d6d6;
  --white:#ffffff;
}
*{box-sizing:border-box;margin:0;padding:0}
html,body{width:673px;height:1200px;overflow:hidden;background:var(--white)}
body{position:relative;font-family:"Roboto",Arial,sans-serif;color:var(--ink)}
.abs{position:absolute}

/* header */
.site-header{left:0;top:0;width:673px;height:34px;background:var(--white)}
.brand-mini{left:40px;top:6px;display:flex;align-items:center;gap:4px;font-size:7px;font-weight:500;color:var(--blue)}
.brand-mini .dot{width:14px;height:14px;border-radius:50%;background:var(--green)}
.nav{top:12px;font-size:8px;color:var(--ink)}
.nav.active{color:var(--green);border-bottom:1px solid var(--green);padding-bottom:1px}
.social{top:11px;width:10px;height:10px;border-radius:50%;background:var(--blue)}

/* hero */
.hero{left:0;top:34px;width:673px;height:234px;background:linear-gradient(90deg,#d9dee3 0%,#eef1f4 45%,#e4eaf0 100%)}
.hero-photo{left:60px;top:34px;width:250px;height:234px;background:linear-gradient(180deg,#c9b2a2 0%,#e9eef2 55%,#f4f6f8 100%)}
.hero-title{left:370px;top:125px;font-size:25px;font-weight:500;color:#444}
.hero-sub{left:392px;top:156px;font-size:16px;font-weight:300;color:var(--blue)}
.btn{background:var(--green);color:var(--white);font-size:7px;font-weight:500;display:flex;align-items:center;justify-content:center;border-radius:8px}

/* about */
.logo{left:80px;top:290px;display:flex;align-items:center;gap:6px;font-size:12px;font-weight:700;color:var(--blue)}
.logo .dot{width:28px;height:28px;border-radius:50%;background:var(--green)}
.bio{left:80px;top:336px;width:365px;font-size:10.5px;line-height:13px;color:#555}
.bio p{margin-bottom:13px}
.btn-outline{left:85px;top:587px;width:72px;height:20px;border:1px solid var(--green);border-radius:4px;font-size:9px;color:var(--green);display:flex;align-items:center;justify-content:center}
.divider{left:466px;top:290px;width:1px;height:350px;background:var(--line)}
.blog-icon{left:480px;top:298px;width:14px;height:14px;border-radius:50%;background:var(--green)}
.blog-kicker{left:498px;top:297px;font-size:9px;color:var(--green)}
.blog-head{left:498px;top:308px;font-size:11px;font-weight:500;color:var(--blue)}
.thumb{left:490px;width:125px;height:62px}
.thumb-cap{left:490px;font-size:10px;font-weight:700;color:var(--blue)}

/* insurance */
.insurance{left:0;top:650px;width:673px;height:212px;background:linear-gradient(90deg,#dcdcdc 0%,#f1f1f1 60%,#fafafa 100%)}
.insurance-photo{left:70px;top:650px;width:270px;height:212px;background:linear-gradient(180deg,#8a5c45 0%,#d8b7a2 45%,#f2e4da 100%)}
.insurance-title{left:378px;top:702px;font-size:24px;line-height:28px;font-weight:400;color:var(--blue)}

/* appointment */
.appointment{left:0;top:862px;width:673px;height:180px;background:linear-gradient(180deg,#1258b0 0%,var(--blue-deep) 100%)}
.appt-title{left:148px;top:912px;font-size:19px;line-height:22px;color:var(--white)}
.field{left:340px;width:160px;height:13px;background:var(--white);border-radius:1px}
.appt-note{left:340px;font-size:6.5px;color:#dbe7f7}
.btn-request{left:448px;top:977px;width:48px;height:17px;border-radius:2px;font-size:9px}

/* footer */
.foot-h{top:1060px;font-size:10px;font-weight:700;color:var(--ink)}
.foot-t{font-size:6.5px;line-height:9px;color:var(--muted)}
.foot-row{left:430px;display:flex;align-items:center;gap:4px;font-size:6.5px;color:var(--muted)}
.foot-row svg{width:7px;height:7px}
.foot-line{left:120px;top:1143px;width:440px;height:1px;background:var(--line)}
.copyright{left:145px;top:1162px;font-size:7.5px;color:var(--muted)}
</style>
</head>
<body>

<header class="abs site-header">
  <div class="abs brand-mini"><span class="dot"></span>The Dental Corner</div>
  <span class="abs nav active" style="left:165px">Home</span>
  <span class="abs nav" style="left:203px">Services</span>
  <span class="abs nav" style="left:248px">About Insurance</span>
  <span class="abs nav" style="left:322px">Se habla español</span>
  <span class="abs nav" style="left:400px">Contact Me</span>
  <span class="abs nav" style="left:536px;color:var(--muted)">Follow us on</span>
  <span class="abs social" style="left:590px"></span>
  <span class="abs social" style="left:605px"></span>
</header>

<section class="abs hero" role="img" aria-label="Bright dental clinic interior"></section>
<div class="abs hero-photo" role="img" aria-label="Portrait of the dentist in a white coat"></div>
<h1 class="abs hero-title">Meet Dr. Elena Marquez</h1>
<p class="abs hero-sub">Dental care is my life</p>
<div class="abs btn" style="left:383px;top:182px;width:60px;height:15px">Read More</div>

<section>
  <div class="abs logo"><span class="dot"></span>THE DENTAL CORNER</div>
  <div class="abs bio">
    <p>Lorem ipsum dolor sit amet, consectetur adipiscing elit, sed do eiusmod tempor incididunt ut labore et dolore magna aliqua. Ut enim ad minim veniam, quis nostrud exercitation ullamco laboris nisi ut aliquip ex ea commodo consequat. Duis aute irure dolor in reprehenderit in voluptate velit esse cillum dolore eu fugiat nulla pariatur. Excepteur sint occaecat cupidatat non proident, sunt in culpa qui officia deserunt mollit anim id est laborum.</p>
    <p>Sed ut perspiciatis unde omnis iste natus error sit voluptatem accusantium doloremque laudantium, totam rem aperiam, eaque ipsa quae ab illo inventore veritatis et quasi architecto beatae vitae dicta sunt explicabo. Nemo enim ipsam voluptatem quia voluptas sit aspernatur aut odit aut fugit, sed quia consequuntur magni dolores eos qui ratione voluptatem sequi nesciunt.</p>
  </div>
  <div class="abs btn-outline">Read More</div>
  <div class="abs divider"></div>

  <aside>
    <span class="abs blog-icon"></span>
    <span class="abs blog-kicker">Read my Blog</span>
    <span class="abs blog-head">Tips for your Dental care</span>
    <div class="abs thumb" style="top:325px;background:linear-gradient(135deg,#cfd6dc,#eef1f3)" role="img" aria-label="Patient holding her cheek in pain"></div>
    <span class="abs thumb-cap" style="top:392px">Where is your pain?</span>
    <div class="abs thumb" style="top:425px;background:linear-gradient(135deg,#b9d3e8,#eaf2f8)" role="img" aria-label="Dentist examining a patient"></div>
    <span class="abs thumb-cap" style="top:501px">Dental care every month</span>
    <div class="abs thumb" style="top:535px;background:linear-gradient(135deg,#e6d2c2,#f5ece4)" role="img" aria-label="Family brushing teeth together"></div>
    <span class="abs thumb-cap" style="top:608px">Cleaning methods</span>
  </aside>
</section>

<section class="abs insurance" role="img" aria-label="Clinic background"></section>
<div class="abs insurance-photo" role="img" aria-label="Smiling woman pointing at her teeth"></div>
<h2 class="abs insurance-title">All Insurance<br>Accepted</h2>
<div class="abs btn" style="left:380px;top:768px;width:60px;height:16px">Read more</div>

<section class="abs appointment"></section>
<h2 class="abs appt-title">Request an<br>Appointment form<br>to notify us</h2>
<div class="abs field" style="top:900px"></div>
<div class="abs field" style="top:918px"></div>
<div class="abs field" style="top:936px"></div>
<div class="abs field" style="top:954px"></div>
<span class="abs appt-note" style="top:976px">Or Call (555) 555-0134</span>
<span class="abs appt-note" style="top:985px">New Pat Text, 6pm PST</span>
<div class="abs btn btn-request">Request</div>

<footer>
  <h3 class="abs foot-h" style="left:309px">Latest Blog</h3>
  <p class="abs foot-t" style="left:309px;top:1075px;width:110px">Lorem ipsum dolor sit amet, consectetur adipiscing elit, sed do eiusmod tempor incididunt ut labore et dolore magna aliqua.</p>
  <h3 class="abs foot-h" style="left:430px">Contact Me</h3>
  <div class="abs foot-row" style="top:1075px"><svg viewBox="0 0 10 10"><path d="M5 0a3.5 3.5 0 0 0-3.5 3.5C1.5 6 5 10 5 10s3.5-4 3.5-6.5A3.5 3.5 0 0 0 5 0z" fill="#777"/></svg>2180 Alder Row, Brindlewood</div>
  <div class="abs foot-row" style="top:1085px;left:441px">Brindlewood, BW 30418</div>
  <div class="abs foot-row" style="top:1096px"><svg viewBox="0 0 10 10"><path d="M2 0l2 2-1 2 3 3 2-1 2 2-2 2C4 10 0 6 0 2z" fill="#777"/></svg>(555) 555-0134</div>
  <div class="abs foot-row" style="top:1106px"><svg viewBox="0 0 10 10"><rect x="0" y="2" width="10" height="6" fill="#777"/></svg>hello@dentalcornerbw.com</div>
  <div class="abs foot-line"></div>
  <p class="abs copyright">© 2016 The Dental Corner</p>
</footer>

</body>
</html>
```